Quill Press Co-op needs a website

We require a website design which will be different to the normal websites that you visit. The objective of this website will be a call to action on the last page which will link to our email address so customers can email us their quotation requirements.

An example of how we envisage the look and the pages turning is as a flip books for example: https://www.vidstreamly.example/watch?v=KpZtLmQaRoX&feature=vid.ly

page 1: just has our logo on it with the tag "Specialist producing quality printed books to your deadline."

Page 2: Black Page with white text "Black and White Book"
These are produced either digitally or offset on a complete range of stocks

Page 3: Colour books (use an image of your choice) These are also produced either digitally or offset plus we have the choice of web presses for larger print runs

Page 4: Digital books We do have a minimum run of 50 books using this process so a one off Thesis is not economically viable using this process. In special circumstance the digital process can produce books more quickly then by using our offset printing process.

Page 5: Having the complete range of printing machines at our disposal enables you to make a perfectly informed choice for your special project.

Then we need a special quote button which takes them directly to our email link. On this page we also need to add: We have had 25 years' experience printing books saving customers time and money whilst guaranteeing quality

Page 6: Logo repeated from page one with name: Morven Tusk and mobile phone no 0481 552 037

- Must follow the brief exactly. Must have a turn page book. Clear, simple and concise with a touch of creative flare and must lead into a call for action which is there quotation. A unique button for quotation link...something out of the ordinary which makes someone want to get a quote.

- It would be nice to have 3D Logo on Page 1 & 6.
a unique button for quotation link...something that make someone eager to proceed.

Our main objective is that they should not leave our website without giving us a quote. Please make sure that the spelling is correct and we do not require clip art images. Continue the logo colours through the theme

here is another example www.vidstreamly.example/watch?v=JQrb204XkWp Added Saturday, May 13, 2017

Target Market(s)

Schools, Universities, Self Publishers, Publishers, Graphic Designers, Conference Providers, Businesses, Corporations, Government.

Industry/Entity Type

Printing

Coding

Coded - Design and coding required

Number of Pages Required

5+ page

Font styles to use
Sans Serif

Colors
34a6d7
ec1f27
fbed22
9bcb3c
ffc214
6b449b

Requirements
Must have
• Must follow the brief exactly. Must have a turn page book. Clear, simple and concise with a touch of creative flare and must lead into a call for action which is there quotation. A unique button for quotation link...something out of the ordinary which makes someone want to get a quote. would like to see the colours of the logo use throughout
Nice to have
• 3D Logo on Page 1 & 6.
• a unique button for quotation link...something that make someone eager to proceed.
• Our main objective is that they should not leave our website without giving us a quote
Should not have
• Spelling mistakes, clip art, ordinary design

```html
<!DOCTYPE html>
<html lang="en">
<head>
<meta charset="utf-8">
<title>Quill Press Co-op – Special Quote</title>
<link rel="stylesheet" href="https://fonts.googleapis.com/css2?family=Roboto:wght@400&display=swap">
<style>
  :root {
    --ink: #444444;
    --paper: #ffffff;
    --leaf: #9bcb3c;
    --quote: #fba01d;
  }
  * { margin: 0; padding: 0; box-sizing: border-box; }
  html, body { width: 720px; height: 1200px; overflow: hidden; }
  body { font-family: "Roboto", Arial, sans-serif; color: var(--ink); background: var(--paper); }
  .page { position: relative; width: 720px; height: 1200px; overflow: hidden; }
  .hero { position: absolute; inset: 0; width: 720px; height: 1200px; }
  .content {
    position: absolute; left: 0; right: 0; top: 612px;
    text-align: center;
  }
  .content p {
    width: 600px; margin: 0 auto;
    font-size: 27px; line-height: 40px; letter-spacing: 0.2px;
  }
  .content .experience { width: 660px; margin-top: 30px; line-height: 42px; }
  .quote-button {
    display: block; width: 236px; height: 46px; margin: 27px auto 0;
    border-radius: 23px; background: var(--quote);
    color: var(--paper); font-size: 24px; line-height: 46px;
    text-decoration: none;
  }
  .ink-splash {
    position: absolute; left: 0; right: 0; bottom: 0; height: 220px;
    background: linear-gradient(90deg, #bfe3f3 0%, #f1c6ee 22%, #f8f2a8 50%, #f6f3c8 68%, #dcdcdc 88%, #f0f0f0 100%);
  }
</style>
</head>
<body>
<main class="page">
  <svg class="hero" viewBox="0 0 720 1200" aria-hidden="true">
    <defs>
      <linearGradient id="press-tones" x1="0" y1="0" x2="1" y2="1">
        <stop offset="0" stop-color="#6d7278"/>
        <stop offset="0.45" stop-color="#8a8f94"/>
        <stop offset="0.7" stop-color="#b7bcc2"/>
        <stop offset="1" stop-color="#e6e8ec"/>
      </linearGradient>
      <linearGradient id="paper-tones" x1="0" y1="0" x2="1" y2="1">
        <stop offset="0" stop-color="#fbfbfb"/>
        <stop offset="1" stop-color="#ececec"/>
      </linearGradient>
    </defs>
    <rect class="press-photo" width="720" height="700" fill="url(#press-tones)" role="img" aria-label="Photo of a wide-format digital printing press at a trade show, printing colourful posters"/>
    <path class="paper-sheet" d="M0 288 C 90 370, 220 395, 380 420 C 520 442, 640 540, 720 680 L720 1200 L0 1200 Z" fill="url(#paper-tones)"/>
    <path class="leaf-edge" d="M0 288 C 90 370, 220 395, 380 420 C 520 442, 640 540, 720 680" fill="none" stroke="var(--leaf)" stroke-width="5"/>
  </svg>

  <section class="content">
    <p>Having the complete range of printing machines at our disposal enables you to make a perfectly informed choice for your special project.</p>
    <p class="experience">We have had 25 years' experience printing<br>books saving customers time and money whilst<br>guaranteeing quality</p>
    <a class="quote-button" href="mailto:quotes@quillpress.example">Special Quote</a>
  </section>

  <div class="ink-splash" role="img" aria-label="Photo of cyan, magenta, yellow and black ink powder bursting along the bottom edge"></div>
</main>
</body>
</html>
```